Four in One (Flexible infographic for Content Management Industry)

See attachment.
A graphic depicting 4 products, where each can stand on its own and each can be combined with others, but where, if all are taken together, the best result is achieved (the "super product").
Intended use is web. See attached file as an example.
The most basic idea is as the attached diagram shows, where 4 rectangles are arranged in a quadrangle, with a middle rectangle in the center representing the combined 4 products. This concept is fine except it is a bit too obvious as it stands. We are looking for either a variation of this or another concept.
The audience is technical + professional + enterprise - NOT consumers. Hence the design should be conservative in nature.
We are aware of tools like as Canva or Pictogram where such graphics are available, but we are looking for something with a bit more imagination and flexibility.
This graphic should be targeted to web sites and be delivered with vector-based (SVG) graphics.

```html
<!DOCTYPE html>
<html lang="en">
<head>
<meta charset="utf-8">
<title>Four in One – Super Product</title>
<link href="https://fonts.googleapis.com/css2?family=Arimo:wght@400;700&display=swap" rel="stylesheet">
<style>
  :root{
    --stage:#393939;
    --panel:#e6e6e6;
    --card:#ffffff;
    --frame:#e4e4e4;
    --head:#2d2d2d;
    --ink:#111111;
    --orange:#ff9410;
    --orange-deep:#f7690f;
    --green:#9dcb0b;
    --green-deep:#74a00f;
    --purple:#7c3cc2;
    --purple-deep:#6a2ea2;
    --blue:#1b7fe8;
    --blue-deep:#0b4cff;
  }
  *{box-sizing:border-box;margin:0;padding:0}
  html,body{width:1200px;height:1200px;overflow:hidden;background:var(--stage);font-family:"Arimo",Arial,sans-serif;color:var(--ink)}
  .panel{position:absolute;left:46px;top:184px;width:1108px;height:831px;background:var(--panel);box-shadow:4px 6px 12px rgba(0,0,0,.35)}
  .card{position:absolute;width:468px;height:320px;background:var(--card);border-radius:52px;box-shadow:6px 8px 10px rgba(0,0,0,.18)}
  .card--tl{left:112px;top:258px}
  .card--tr{left:615px;top:258px}
  .card--bl{left:112px;top:614px}
  .card--br{left:615px;top:614px}
  .frame{position:absolute;left:37px;top:35px;width:394px;height:245px;border:2px solid var(--frame);border-top:none}
  .card--tl .frame,.card--bl .frame{border-bottom-right-radius:30px}
  .card--tr .frame,.card--br .frame{border-bottom-left-radius:30px}
  .card--bl .frame,.card--br .frame{top:44px;height:245px}
  .heading{position:absolute;left:-2px;top:0;width:394px;height:34px;background:var(--head);color:#fff;font-weight:700;font-size:17px;line-height:34px;padding:0 35px}
  .card--tl .heading,.card--bl .heading{border-top-right-radius:30px}
  .card--tr .heading,.card--br .heading{border-top-left-radius:30px;text-align:right}
  .desc{position:absolute;top:42px;font-size:13px;line-height:20px;white-space:nowrap}
  .card--tl .desc,.card--bl .desc{left:35px}
  .card--tr .desc,.card--br .desc{right:35px;text-align:right}
  .features{position:absolute;top:107px;list-style:none}
  .features li{display:flex;align-items:center;gap:13px;height:24.6px;font-weight:700;font-size:13px;white-space:nowrap}
  .card--tl .features,.card--bl .features{left:34px}
  .card--tr .features,.card--br .features{right:30px}
  .card--tr .features li,.card--br .features li{flex-direction:row-reverse;gap:17px}
  .tick{width:12px;height:12px;flex:none}
  .btn{position:absolute;top:216px;width:91px;height:19px;border-radius:10px;color:#fff;font-size:13px;line-height:19px;text-align:center}
  .card--tl .btn,.card--bl .btn{left:36px}
  .card--tr .btn,.card--br .btn{right:37px}
  .card--tl .btn{background:var(--orange)}
  .card--tr .btn{background:var(--green)}
  .card--bl .btn{background:var(--purple)}
  .card--br .btn{background:var(--blue)}
  .hub{position:absolute;left:0;top:0;width:1200px;height:1200px;pointer-events:none}
  .hub-title{position:absolute;left:501px;top:616px;width:200px;text-align:center;font-weight:700;font-size:30px;line-height:34px;color:#111}
</style>
</head>
<body>
<div class="panel"></div>

<section class="card card--tl">
  <div class="frame">
    <h2 class="heading">Document Management</h2>
    <p class="desc">Streamline document organization, access, and<br>collaboration with easier file storage and sharing,<br>leading to more efficient workflows.</p>
    <ul class="features">
      <li><svg class="tick" viewBox="0 0 12 12"><circle cx="6" cy="6" r="6" fill="var(--orange)"/><path d="M3.2 6.2l2 2 3.6-4" fill="none" stroke="#fff" stroke-width="1.5"/></svg>Centralized Document Control</li>
      <li><svg class="tick" viewBox="0 0 12 12"><circle cx="6" cy="6" r="6" fill="var(--orange)"/><path d="M3.2 6.2l2 2 3.6-4" fill="none" stroke="#fff" stroke-width="1.5"/></svg>Collaborative Workspace Integration</li>
      <li><svg class="tick" viewBox="0 0 12 12"><circle cx="6" cy="6" r="6" fill="var(--orange)"/><path d="M3.2 6.2l2 2 3.6-4" fill="none" stroke="#fff" stroke-width="1.5"/></svg>Automated Compliance Tracking</li>
      <li><svg class="tick" viewBox="0 0 12 12"><circle cx="6" cy="6" r="6" fill="var(--orange)"/><path d="M3.2 6.2l2 2 3.6-4" fill="none" stroke="#fff" stroke-width="1.5"/></svg>Check 4</li>
    </ul>
    <span class="btn">Learn More</span>
  </div>
</section>

<section class="card card--tr">
  <div class="frame">
    <h2 class="heading">Security and Compliance</h2>
    <p class="desc">Benefit from tailored cloud solutions, secured data<br>storage, and expert disaster recovery planning for<br>reliable and scalable IT operations.</p>
    <ul class="features">
      <li><svg class="tick" viewBox="0 0 12 12"><circle cx="6" cy="6" r="6" fill="var(--green)"/><path d="M3.2 6.2l2 2 3.6-4" fill="none" stroke="#fff" stroke-width="1.5"/></svg>Custom Cloud Solutions</li>
      <li><svg class="tick" viewBox="0 0 12 12"><circle cx="6" cy="6" r="6" fill="var(--green)"/><path d="M3.2 6.2l2 2 3.6-4" fill="none" stroke="#fff" stroke-width="1.5"/></svg>Secure Data Storage</li>
      <li><svg class="tick" viewBox="0 0 12 12"><circle cx="6" cy="6" r="6" fill="var(--green)"/><path d="M3.2 6.2l2 2 3.6-4" fill="none" stroke="#fff" stroke-width="1.5"/></svg>Expert Disaster Recovery</li>
      <li><svg class="tick" viewBox="0 0 12 12"><circle cx="6" cy="6" r="6" fill="var(--green)"/><path d="M3.2 6.2l2 2 3.6-4" fill="none" stroke="#fff" stroke-width="1.5"/></svg>Check 4</li>
    </ul>
    <span class="btn">Learn More</span>
  </div>
</section>

<section class="card card--bl">
  <div class="frame">
    <h2 class="heading">Enterprise Resource Planning</h2>
    <p class="desc">Simplify management across finance,<br>sales, and operations, enabling better<br>decision-making and improved productivity.</p>
    <ul class="features">
      <li><svg class="tick" viewBox="0 0 12 12"><circle cx="6" cy="6" r="6" fill="var(--purple)"/><path d="M3.2 6.2l2 2 3.6-4" fill="none" stroke="#fff" stroke-width="1.5"/></svg>Integrated Business Processes</li>
      <li><svg class="tick" viewBox="0 0 12 12"><circle cx="6" cy="6" r="6" fill="var(--purple)"/><path d="M3.2 6.2l2 2 3.6-4" fill="none" stroke="#fff" stroke-width="1.5"/></svg>Enhanced Decision-Making</li>
      <li><svg class="tick" viewBox="0 0 12 12"><circle cx="6" cy="6" r="6" fill="var(--purple)"/><path d="M3.2 6.2l2 2 3.6-4" fill="none" stroke="#fff" stroke-width="1.5"/></svg>Productivity Improvement</li>
      <li><svg class="tick" viewBox="0 0 12 12"><circle cx="6" cy="6" r="6" fill="var(--purple)"/><path d="M3.2 6.2l2 2 3.6-4" fill="none" stroke="#fff" stroke-width="1.5"/></svg>Check 4</li>
    </ul>
    <span class="btn">Learn More</span>
  </div>
</section>

<section class="card card--br">
  <div class="frame">
    <h2 class="heading">Digital Transformation</h2>
    <p class="desc">Turn scanned documents into easily<br>searchable digital archives, boosting<br>efficiency and accessibility.</p>
    <ul class="features">
      <li><svg class="tick" viewBox="0 0 12 12"><circle cx="6" cy="6" r="6" fill="var(--blue)"/><path d="M3.2 6.2l2 2 3.6-4" fill="none" stroke="#fff" stroke-width="1.5"/></svg>Instant searchable Archives with OCR</li>
      <li><svg class="tick" viewBox="0 0 12 12"><circle cx="6" cy="6" r="6" fill="var(--blue)"/><path d="M3.2 6.2l2 2 3.6-4" fill="none" stroke="#fff" stroke-width="1.5"/></svg>Automated Document Classification</li>
      <li><svg class="tick" viewBox="0 0 12 12"><circle cx="6" cy="6" r="6" fill="var(--blue)"/><path d="M3.2 6.2l2 2 3.6-4" fill="none" stroke="#fff" stroke-width="1.5"/></svg>DocuVault and Cloud Blob Ready</li>
      <li><svg class="tick" viewBox="0 0 12 12"><circle cx="6" cy="6" r="6" fill="var(--blue)"/><path d="M3.2 6.2l2 2 3.6-4" fill="none" stroke="#fff" stroke-width="1.5"/></svg>Check 4</li>
    </ul>
    <span class="btn">Learn More</span>
  </div>
</section>

<svg class="hub" viewBox="0 0 1200 1200" aria-hidden="true">
  <defs>
    <clipPath id="q-tl"><rect x="0" y="0" width="579" height="578"/></clipPath>
    <clipPath id="q-tr"><rect x="615" y="0" width="585" height="578"/></clipPath>
    <clipPath id="q-bl"><rect x="0" y="614" width="579" height="586"/></clipPath>
    <clipPath id="q-br"><rect x="615" y="614" width="585" height="586"/></clipPath>
    <radialGradient id="core" cx="45%" cy="35%" r="70%">
      <stop offset="0" stop-color="#ffffff"/><stop offset="0.6" stop-color="#f1f1f1"/><stop offset="1" stop-color="#cfcfcf"/>
    </radialGradient>
    <linearGradient id="rim" x1="0" y1="0" x2="0" y2="1">
      <stop offset="0" stop-color="#d2d2d2"/><stop offset="1" stop-color="#f4f4f4"/>
    </linearGradient>
    <filter id="soft" x="-30%" y="-30%" width="160%" height="160%"><feDropShadow dx="2" dy="4" stdDeviation="5" flood-opacity=".25"/></filter>
  </defs>

  <g class="ring" fill="none" stroke-width="56">
    <circle cx="601" cy="593" r="153" stroke="var(--orange)" clip-path="url(#q-tl)"/>
    <circle cx="601" cy="593" r="153" stroke="var(--green)" clip-path="url(#q-tr)"/>
    <circle cx="601" cy="593" r="153" stroke="var(--purple)" clip-path="url(#q-bl)"/>
    <circle cx="601" cy="593" r="153" stroke="var(--blue)" clip-path="url(#q-br)"/>
  </g>

  <circle cx="601" cy="593" r="131" fill="#fafafa" filter="url(#soft)"/>
  <circle cx="601" cy="593" r="124" fill="url(#rim)"/>
  <circle cx="601" cy="593" r="106" fill="url(#core)" filter="url(#soft)"/>

  <g class="hub-icon" fill="#1a1a1a">
    <path d="M601 502l4 9 10 1-7.5 6.5 2.5 10-9-5.5-9 5.5 2.5-10-7.5-6.5 10-1z"/>
    <path d="M575 514l2.4 5 5.6.6-4.2 3.8 1.2 5.5-5-3-5 3 1.2-5.5-4.2-3.8 5.6-.6z"/>
    <path d="M628 514l2.4 5 5.6.6-4.2 3.8 1.2 5.5-5-3-5 3 1.2-5.5-4.2-3.8 5.6-.6z"/>
    <g stroke="#1a1a1a" stroke-width="2.6" stroke-linecap="round">
      <line x1="576" y1="534" x2="580" y2="545"/><line x1="588" y1="530" x2="590" y2="543"/>
      <line x1="601" y1="530" x2="601" y2="543"/><line x1="614" y1="530" x2="612" y2="543"/>
      <line x1="626" y1="534" x2="622" y2="545"/>
    </g>
    <rect x="567" y="551" width="70" height="48" rx="3"/>
    <path d="M561 601h82v5h-82z"/>
    <path d="M613 561l-14 2 5 4-10 10 4 4 10-10 4 5z" fill="#fff"/>
  </g>

  <g class="badge badge--doc" filter="url(#soft)">
    <circle cx="489" cy="487" r="45" fill="#fff"/>
    <circle cx="489" cy="487" r="42" fill="var(--orange-deep)"/>
    <path d="M477 466h16l8 8v36h-24z" fill="#fff"/>
    <path d="M493 466v8h8" fill="none" stroke="var(--orange-deep)" stroke-width="1.6"/>
    <g stroke="var(--orange-deep)" stroke-width="2"><line x1="482" y1="484" x2="496" y2="484"/><line x1="482" y1="489" x2="496" y2="489"/><line x1="482" y1="494" x2="496" y2="494"/><line x1="482" y1="499" x2="492" y2="499"/></g>
  </g>

  <g class="badge badge--cloud" filter="url(#soft)">
    <circle cx="711" cy="487" r="45" fill="#fff"/>
    <circle cx="711" cy="487" r="42" fill="var(--green-deep)"/>
    <path d="M696 498a10 10 0 0 1 0-20a14 14 0 0 1 27-3a11 11 0 0 1 3 23z" fill="#fff"/>
    <path d="M711 478l11 4v8c0 7-5 12-11 15c-6-3-11-8-11-15v-8z" fill="var(--green-deep)"/>
    <path d="M711 482l7 3v5c0 5-3 8-7 10c-4-2-7-5-7-10v-5z" fill="#fff"/>
    <path d="M707 490l3 3 5-6" fill="none" stroke="var(--green-deep)" stroke-width="2"/>
  </g>

  <g class="badge badge--erp" filter="url(#soft)">
    <circle cx="489" cy="700" r="45" fill="#fff"/>
    <circle cx="489" cy="700" r="42" fill="var(--purple-deep)"/>
    <rect x="472" y="683" width="34" height="34" fill="none" stroke="#fff" stroke-width="3"/>
    <g fill="#fff"><circle cx="472" cy="683" r="5"/><circle cx="506" cy="683" r="5"/><circle cx="472" cy="717" r="5"/><circle cx="506" cy="717" r="5"/>
    <rect x="480" y="698" width="5" height="12"/><rect x="487" y="692" width="5" height="18"/><rect x="494" y="701" width="5" height="9"/></g>
  </g>

  <g class="badge badge--digital" filter="url(#soft)">
    <circle cx="711" cy="700" r="45" fill="#fff"/>
    <circle cx="711" cy="700" r="42" fill="var(--blue-deep)"/>
    <path d="M711 681a19 19 0 0 0 0 38" fill="none" stroke="#fff" stroke-width="7" stroke-dasharray="5 3"/>
    <path d="M711 689a11 11 0 0 0 0 22" fill="none" stroke="#fff" stroke-width="4"/>
    <g stroke="#fff" stroke-width="2.4" fill="none"><path d="M711 686h6l4-4"/><path d="M711 694h12"/><path d="M711 706h12"/><path d="M711 714h6l4 4"/><path d="M711 700h15"/></g>
    <g fill="#fff"><circle cx="723" cy="681" r="3"/><circle cx="726" cy="694" r="3"/><circle cx="729" cy="700" r="3"/><circle cx="726" cy="706" r="3"/><circle cx="723" cy="719" r="3"/></g>
  </g>
</svg>

<div class="hub-title">Super<br>Product</div>
</body>
</html>
```